Simple, elegant, business card design required

Hi designers,I am looking for a simple yet elegant business card design.

Please make use of my logo (attached); you are free to tweak the logo should you wish to do so.

Our business is involved in many different fields - almost all of them involved in some form of "design", so that's really one of the key things I want to portray. I do not wish to specify which field of design, exactly.

I prefer white on black (or just monochromatic), but if you have a different, creative idea, I am open to that too.

You can use artsy photographs provided that you have the license to use those. Please feel free to ask me any questions.

Target Market(s)

High-end customers looking for design consultancy

Industry/Entity Type

Business

Contact Information for Business Card

Name: Gareth Pellwinter
Position: Creative Director
Mobile: +150963218745
Address: Morrow Lane, Ashcombe Vale, Haverleigh HV4 2JT
Website: corvastudio.com (not launched yet)

Requirements
Must have
• Design layout must be clean, original, and text must be readable when printed.
Should not have
• ~ No business card templates please. Anyone using this will be reported.
• ~ Please don't spam entries.

```html
<!DOCTYPE html>
<html lang="en">
<head>
<meta charset="utf-8">
<title>Corva Studio — Business Card</title>
<link rel="stylesheet" href="https://fonts.googleapis.com/css2?family=Open+Sans:wght@400;500&display=swap">
<style>
  :root {
    --stage: #e9e7e4;
    --ink: #1f1e20;
    --card-black: #232224;
    --pattern-tone: #2b2a2c;
    --paper: #ffffff;
    --rule: #232224;
  }
  * { margin: 0; padding: 0; box-sizing: border-box; }
  html, body { width: 1200px; height: 1000px; overflow: hidden; }
  body {
    background: var(--stage);
    position: relative;
    font-family: "Open Sans", sans-serif;
    color: var(--ink);
  }

  /* Back of card */
  .card-back {
    position: absolute;
    left: 120px; top: 70px;
    width: 800px; height: 440px;
    background: var(--card-black);
  }
  .card-back__pattern {
    position: absolute; inset: 0;
    background: radial-gradient(circle at 60% 45%, var(--pattern-tone), var(--card-black) 75%);
  }
  .card-back__mark {
    position: absolute;
    left: 540px; top: 160px;
    display: flex; align-items: center; gap: 10px;
    color: var(--paper);
    font-size: 16px; font-weight: 500;
    letter-spacing: 0.28em;
  }
  .card-back__dot {
    width: 14px; height: 14px; border: 2px solid var(--paper); border-radius: 50%;
  }

  /* Front of card */
  .card-front {
    position: absolute;
    left: 200px; top: 440px;
    width: 800px; height: 420px;
    background: var(--paper);
    box-shadow: 0 14px 0 var(--card-black);
  }
  .brand {
    position: absolute;
    left: 55px; top: 64px;
    display: flex; align-items: center; gap: 22px;
  }
  .brand__circle {
    width: 50px; height: 50px;
    border: 5px solid var(--ink); border-radius: 50%;
  }
  .brand__name {
    font-size: 38px; font-weight: 500;
    letter-spacing: 0.2em;
    line-height: 1;
  }

  .title-row {
    position: absolute; left: 0; right: 30px; top: 168px;
    display: flex; align-items: flex-start;
  }
  .title-row__rule {
    height: 4px; background: var(--rule); margin-top: 24px;
  }
  .title-row__rule--left { flex: 0 0 450px; }
  .title-row__rule--right { flex: 1; }
  .person { padding: 0 10px; }
  .person__name { font-size: 24px; font-weight: 400; line-height: 1.2; white-space: nowrap; }
  .person__role { font-size: 18px; margin-top: 2px; }

  .contacts {
    position: absolute; left: 52px; top: 245px;
    list-style: none;
    font-size: 20px;
  }
  .contacts__item {
    display: flex; align-items: center; gap: 12px;
    height: 33px;
  }
  .contacts__icon { width: 18px; height: 20px; flex: none; }
  .address {
    position: absolute; left: 52px; top: 330px;
    font-size: 20px; line-height: 1.5; font-style: normal;
  }
</style>
</head>
<body>
  <section class="card-back" aria-label="Card back">
    <div class="card-back__pattern" role="img" aria-label="Repeating tone-on-tone brand pattern across the black card back"></div>
    <div class="card-back__mark"><span class="card-back__dot"></span>CORVA STUDIO</div>
  </section>

  <section class="card-front" aria-label="Card front">
    <div class="brand">
      <span class="brand__circle"></span>
      <span class="brand__name">CORVA STUDIO</span>
    </div>

    <div class="title-row">
      <div class="title-row__rule title-row__rule--left"></div>
      <div class="person">
        <p class="person__name">Gareth Pellwinter</p>
        <p class="person__role">Creative Director</p>
      </div>
      <div class="title-row__rule title-row__rule--right"></div>
    </div>

    <ul class="contacts">
      <li class="contacts__item">
        <svg class="contacts__icon" viewBox="0 0 18 20" aria-hidden="true">
          <rect x="4" y="2" width="10" height="17" rx="1.5" fill="none" stroke="var(--ink)" stroke-width="2"/>
          <rect x="6.5" y="5" width="5" height="5" fill="var(--ink)"/>
          <circle cx="9" cy="15" r="1.2" fill="var(--ink)"/>
        </svg>
        <span>+150963218745</span>
      </li>
      <li class="contacts__item">
        <svg class="contacts__icon" viewBox="0 0 18 20" aria-hidden="true">
          <circle cx="9" cy="10" r="7.5" fill="var(--ink)"/>
          <path d="M1.5 10h15M9 2.5c-3 3-3 12 0 15M9 2.5c3 3 3 12 0 15" fill="none" stroke="var(--paper)" stroke-width="1"/>
        </svg>
        <span>www.corvastudio.com</span>
      </li>
    </ul>

    <address class="address">
      Morrow Lane, Ashcombe Vale,<br>
      Haverleigh HV4 2JT
    </address>
  </section>
</body>
</html>
```